Business Card Design Project

We are an agricultural business based in Brisbane.
We design, manage and operate regional saleyards. Our logo is green/silver in colour and details of our business can be found on our website www.vodemarketyards.com.au

Just wanting a corporate design for some business cards and include name, position, contact details.

Thanks

Industry/Entity Type

Business

```html
<!DOCTYPE html>
<html lang="en">
<head>
<meta charset="utf-8">
<title>Vode Market Yards – Business Card Options</title>
<link rel="stylesheet" href="https://fonts.googleapis.com/css2?family=PT+Sans+Narrow:wght@400;700&family=Arimo:wght@400&display=swap">
<style>
  :root {
    --backdrop: #2b2b2b;
    --green: #00873e;
    --white: #ffffff;
    --grey: #cfd0d2;
    --ink: #231f20;
    --yellow: #f6e92a;
    --orange: #f8b51c;
    --pale: #fdf9c4;
  }
  * { box-sizing: border-box; margin: 0; padding: 0; }
  html, body { width: 1200px; height: 797px; overflow: hidden; }
  body { background: var(--backdrop); position: relative; font-family: "Arimo", Arial, sans-serif; }
  .gradient-defs { position: absolute; width: 0; height: 0; }
  .card {
    position: absolute; width: 526px; height: 300px; overflow: hidden;
    background: var(--white);
    box-shadow: 2px 3px 6px rgba(0,0,0,.55);
  }
  .card--a { left: 45px;  top: 78px; }
  .card--b { left: 614px; top: 78px; }
  .card--c { left: 45px;  top: 428px; }
  .card--d { left: 614px; top: 428px; }
  .card__art { position: absolute; inset: 0; width: 526px; height: 300px; }
  .wordmark {
    position: absolute; left: 0; right: 0; top: 26px; text-align: center;
    font-family: "PT Sans Narrow", "Arial Narrow", sans-serif; font-weight: 700;
    font-size: 31px; line-height: 29px; letter-spacing: .5px; text-transform: uppercase;
    color: var(--ink);
  }
  .holder { position: absolute; left: 16px; top: 222px; font-family: "PT Sans Narrow", "Arial Narrow", sans-serif; }
  .holder__name { font-size: 31px; font-weight: 700; line-height: 34px; }
  .holder__role { font-family: "Arimo", Arial, sans-serif; font-size: 15.5px; line-height: 22px; }
  .contact { position: absolute; left: 290px; right: 10px; top: 229px; list-style: none; font-size: 14.5px; white-space: nowrap; }
  .contact li { display: flex; align-items: center; height: 23px; }
  .contact svg { flex: none; width: 20px; height: 16px; margin-right: 8px; fill: none; stroke: currentColor; stroke-width: 1.3; }
  .on-green { color: var(--white); }
  .on-light { color: var(--ink); }
</style>
</head>
<body>

<svg class="gradient-defs" aria-hidden="true">
  <defs>
    <linearGradient id="sunband" x1="0" y1="0" x2="1" y2="0">
      <stop offset="0" stop-color="#f7ec5a"/>
      <stop offset=".3" stop-color="#fdf9c4"/>
      <stop offset=".7" stop-color="#f6e92a"/>
      <stop offset="1" stop-color="#f8b51c"/>
    </linearGradient>
    <linearGradient id="trim" x1="0" y1="0" x2="1" y2="0">
      <stop offset="0" stop-color="#f8b51c"/>
      <stop offset=".4" stop-color="#f6e92a"/>
      <stop offset="1" stop-color="#f8b51c"/>
    </linearGradient>
  </defs>
</svg>

<!-- Option A: white top, green base, gold trim -->
<section class="card card--a">
  <svg class="card__art" viewBox="0 0 526 300" aria-hidden="true">
    <path d="M0,92 C120,77 250,152 330,187 C400,217 432,217 442,182 C452,132 470,92 526,96 L526,300 L0,300 Z" fill="url(#trim)"/>
    <path d="M0,102 C120,87 250,162 330,197 C400,227 444,225 452,192 C462,140 480,104 526,106 L526,300 L0,300 Z" fill="var(--green)"/>
  </svg>
  <h1 class="wordmark">Vode Market<br>Yards</h1>
  <div class="holder on-green"><p class="holder__name">Dale Whitford</p><p class="holder__role">Managing Director</p></div>
  <ul class="contact on-green">
    <li><svg viewBox="0 0 20 16"><rect x="1.5" y="2.5" width="17" height="11"/><path d="M1.5,2.5 L10,9.5 L18.5,2.5"/></svg>dale@vodeyards.com.au</li>
    <li><svg viewBox="0 0 20 16"><circle cx="10" cy="8" r="7"/><path d="M7,4.5 C6,8 8,11.5 12,12 L13,10.5 L11.5,9.5 L10.5,10.2 C9.5,9.6 8.7,8.5 8.6,7.3 L9.6,6.7 L9,5 Z"/></svg>0400 555 019</li>
    <li><svg viewBox="0 0 20 16"><ellipse cx="9" cy="10" rx="7" ry="5"/><path d="M9,5 V9 M2,9.5 H16 M12,5.5 C14,2 17,3 19,1"/></svg>www.vodemarketyards.com.au</li>
  </ul>
</section>

<!-- Option B: gold top, white base, green trim -->
<section class="card card--b">
  <svg class="card__art" viewBox="0 0 526 300" aria-hidden="true">
    <rect width="526" height="300" fill="url(#sunband)"/>
    <path d="M0,92 C120,77 250,152 330,187 C400,217 432,217 442,182 C452,132 470,102 526,110 L526,300 L0,300 Z" fill="var(--green)"/>
    <path d="M0,102 C120,87 250,162 330,197 C400,227 444,225 452,192 C462,140 480,114 526,120 L526,300 L0,300 Z" fill="var(--white)"/>
  </svg>
  <h1 class="wordmark">Vode Market<br>Yards</h1>
  <div class="holder on-light"><p class="holder__name">Dale Whitford</p><p class="holder__role">Managing Director</p></div>
  <ul class="contact on-light">
    <li><svg viewBox="0 0 20 16"><rect x="1.5" y="2.5" width="17" height="11"/><path d="M1.5,2.5 L10,9.5 L18.5,2.5"/></svg>dale@vodeyards.com.au</li>
    <li><svg viewBox="0 0 20 16"><circle cx="10" cy="8" r="7"/><path d="M7,4.5 C6,8 8,11.5 12,12 L13,10.5 L11.5,9.5 L10.5,10.2 C9.5,9.6 8.7,8.5 8.6,7.3 L9.6,6.7 L9,5 Z"/></svg>0400 555 019</li>
    <li><svg viewBox="0 0 20 16"><ellipse cx="9" cy="10" rx="7" ry="5"/><path d="M9,5 V9 M2,9.5 H16 M12,5.5 C14,2 17,3 19,1"/></svg>www.vodemarketyards.com.au</li>
  </ul>
</section>

<!-- Option C: gold top, grey base, green trim -->
<section class="card card--c">
  <svg class="card__art" viewBox="0 0 526 300" aria-hidden="true">
    <rect width="526" height="300" fill="url(#sunband)"/>
    <path d="M0,88 C120,73 250,148 330,183 C400,213 432,213 442,178 C452,128 470,98 526,106 L526,300 L0,300 Z" fill="var(--green)"/>
    <path d="M0,98 C120,83 250,158 330,193 C400,223 444,221 452,188 C462,136 480,110 526,116 L526,300 L0,300 Z" fill="var(--grey)"/>
  </svg>
  <h1 class="wordmark">Vode Market<br>Yards</h1>
  <div class="holder on-light"><p class="holder__name">Dale Whitford</p><p class="holder__role">Managing Director</p></div>
  <ul class="contact on-light">
    <li><svg viewBox="0 0 20 16"><rect x="1.5" y="2.5" width="17" height="11"/><path d="M1.5,2.5 L10,9.5 L18.5,2.5"/></svg>dale@vodeyards.com.au</li>
    <li><svg viewBox="0 0 20 16"><circle cx="10" cy="8" r="7"/><path d="M7,4.5 C6,8 8,11.5 12,12 L13,10.5 L11.5,9.5 L10.5,10.2 C9.5,9.6 8.7,8.5 8.6,7.3 L9.6,6.7 L9,5 Z"/></svg>0400 555 019</li>
    <li><svg viewBox="0 0 20 16"><ellipse cx="9" cy="10" rx="7" ry="5"/><path d="M9,5 V9 M2,9.5 H16 M12,5.5 C14,2 17,3 19,1"/></svg>www.vodemarketyards.com.au</li>
  </ul>
</section>

<!-- Option D: gold top, green base, white trim -->
<section class="card card--d">
  <svg class="card__art" viewBox="0 0 526 300" aria-hidden="true">
    <rect width="526" height="300" fill="url(#sunband)"/>
    <path d="M0,92 C120,77 250,152 330,187 C400,217 432,217 442,182 C452,132 470,102 526,110 L526,300 L0,300 Z" fill="var(--white)"/>
    <path d="M0,102 C120,87 250,162 330,197 C400,227 444,225 452,192 C462,140 480,114 526,120 L526,300 L0,300 Z" fill="var(--green)"/>
  </svg>
  <h1 class="wordmark">Vode Market<br>Yards</h1>
  <div class="holder on-green"><p class="holder__name">Dale Whitford</p><p class="holder__role">Managing Director</p></div>
  <ul class="contact on-green">
    <li><svg viewBox="0 0 20 16"><rect x="1.5" y="2.5" width="17" height="11"/><path d="M1.5,2.5 L10,9.5 L18.5,2.5"/></svg>dale@vodeyards.com.au</li>
    <li><svg viewBox="0 0 20 16"><circle cx="10" cy="8" r="7"/><path d="M7,4.5 C6,8 8,11.5 12,12 L13,10.5 L11.5,9.5 L10.5,10.2 C9.5,9.6 8.7,8.5 8.6,7.3 L9.6,6.7 L9,5 Z"/></svg>0400 555 019</li>
    <li><svg viewBox="0 0 20 16"><ellipse cx="9" cy="10" rx="7" ry="5"/><path d="M9,5 V9 M2,9.5 H16 M12,5.5 C14,2 17,3 19,1"/></svg>www.vodemarketyards.com.au</li>
  </ul>
</section>

</body>
</html>
```